K&T Holdings

Design a modern simple business card. I have attached a clean version of a card we like form Marrowfield Partners another company we own. I also attached the old K&T card design and logo and a couple of ideas we had but just can't finalize on whether we like them or not. We would like to include the 20 year logo somewhere on the card.

```html
<!DOCTYPE html>
<html lang="en">
<head>
<meta charset="utf-8">
<title>K&amp;T Holdings Business Card</title>
<link rel="stylesheet" href="https://fonts.googleapis.com/css2?family=Barlow:wght@400;500;700;800&display=swap">
<style>
  :root {
    --navy: #26287a;
    --grey: #8a8a8a;
    --card: #f7f7f8;
    --card-shade: #ececee;
    --backdrop: #2a2a2c;
    --white: #ffffff;
  }
  * { box-sizing: border-box; margin: 0; padding: 0; }
  html, body { width: 1200px; height: 800px; overflow: hidden; }
  body {
    background: var(--backdrop);
    font-family: "Barlow", Arial, sans-serif;
    color: var(--navy);
    position: relative;
  }
  .card {
    position: absolute;
    left: 320px;
    width: 560px;
    height: 320px;
    background: linear-gradient(135deg, var(--card) 0%, var(--card-shade) 50%, var(--card) 100%);
    overflow: hidden;
  }
  .card-front { top: 60px; }
  .card-back { top: 420px; }

  /* Front */
  .brand-mark {
    position: absolute;
    left: 34px; top: 88px;
    display: flex; align-items: center; gap: 10px;
    font-weight: 800; font-size: 30px; color: var(--navy);
  }
  .brand-mark .dot { width: 16px; height: 16px; background: var(--navy); border-radius: 50%; }
  .person { position: absolute; left: 250px; top: 58px; }
  .person-name { font-weight: 800; font-size: 26px; letter-spacing: 0.5px; text-transform: uppercase; }
  .person-title { font-weight: 700; font-size: 18px; color: var(--grey); margin-top: 2px; }
  .contact-bar {
    position: absolute; left: 250px; top: 150px;
    width: 28px; height: 170px;
    background: var(--navy); border-radius: 14px 14px 0 0;
  }
  .contact-icon {
    position: absolute; left: 4px;
    width: 20px; height: 20px; border-radius: 50%;
    background: var(--white);
    display: flex; align-items: center; justify-content: center;
  }
  .contact-icon.mail { top: 6px; }
  .contact-icon.phone { top: 32px; }
  .contact-list { position: absolute; left: 288px; top: 140px; font-size: 14px; line-height: 1.35; }
  .contact-list li { list-style: none; }
  .contact-list .email { margin-bottom: 6px; }

  /* Back */
  .office { position: absolute; top: 40px; width: 100%; text-align: center; }
  .office-label { font-weight: 700; font-size: 15px; }
  .office-address { font-size: 14px; }
  .mark-rule { position: absolute; height: 2px; background: var(--navy); }
  .mark-rule.left { left: 20px; width: 150px; top: 164px; }
  .mark-rule.right { right: 20px; width: 150px; top: 136px; }
  .back-mark {
    position: absolute; left: 0; right: 0; top: 130px;
    text-align: center; font-weight: 800; font-size: 32px; color: var(--navy);
  }
  .services { position: absolute; bottom: 30px; width: 100%; text-align: center; }
  .services-heading { font-weight: 700; font-size: 16px; }
  .services-list { display: flex; justify-content: center; gap: 14px; font-size: 14px; margin-top: 4px; }
  .services-list li { list-style: none; }
</style>
</head>
<body>
  <section class="card card-front" aria-label="Card front">
    <div class="brand-mark"><span class="dot"></span>K&amp;T Holdings</div>
    <div class="person">
      <h1 class="person-name">Dana Holloway</h1>
      <p class="person-title">IT Director</p>
    </div>
    <div class="contact-bar">
      <span class="contact-icon mail">
        <svg width="12" height="9" viewBox="0 0 12 9"><rect x="0.5" y="0.5" width="11" height="8" fill="none" stroke="#26287a"/><path d="M0.5 0.5 L6 5 L11.5 0.5" fill="none" stroke="#26287a"/></svg>
      </span>
      <span class="contact-icon phone">
        <svg width="11" height="11" viewBox="0 0 24 24"><path fill="#26287a" d="M6.6 10.8a15.1 15.1 0 0 0 6.6 6.6l2.2-2.2c.3-.3.7-.4 1-.2 1.1.4 2.3.6 3.6.6.6 0 1 .4 1 1V20c0 .6-.4 1-1 1A17 17 0 0 1 3 4c0-.6.4-1 1-1h3.5c.6 0 1 .4 1 1 0 1.3.2 2.5.6 3.6.1.3 0 .7-.2 1z"/></svg>
      </span>
    </div>
    <ul class="contact-list">
      <li class="email">dholloway@ktltd.com</li>
      <li>555-201-4417</li>
      <li>555-318-2064</li>
    </ul>
  </section>

  <section class="card card-back" aria-label="Card back">
    <div class="office">
      <p class="office-label">Corporate:</p>
      <p class="office-address">120 Cedar Avenue, Suite 410, Harlow, TX 75001</p>
    </div>
    <span class="mark-rule left"></span>
    <span class="mark-rule right"></span>
    <div class="back-mark">K&amp;T Holdings</div>
    <div class="services">
      <p class="services-heading">Integrated Industrial Services</p>
      <ul class="services-list">
        <li>Mechanical/Civil</li>
        <li>I&amp;E</li>
        <li>Fabrication</li>
        <li>Rotating Heat Transfer Equipment</li>
      </ul>
    </div>
  </section>
</body>
</html>
```